VELDA Metals - newly established Metal trading business

Velda Metals is a newly established Metal trading, processing and refining business

we are looking for a simple and professional business website, which is easy to navigate

We will be selling metal / commodities to some of the largest industrial business globally. Therefore the website must make us look like a large and reputable business.

We have attached a Powerpoint presentation with some ideas

Target Market(s)

Lagre metal consumers

Industry/Entity Type

Commodity

Logo Text

VELDA Metals Group

Coding

Coded - Design and coding required

Number of Pages Required

5+ page

Font styles to use
Sans Serif

Colors

Designer to choose colors to be used in the design.

Requirements
Must have
• - fixed menu bar at the top
• - continuous scroll down function
• - multiple tabs left and right for more information
• - have dynamic screen size adjustment / a mobile version
• - google maps

```html
<!DOCTYPE html>
<html lang="en">
<head>
<meta charset="utf-8">
<title>Velda Metals</title>
<link href="https://fonts.googleapis.com/css2?family=Montserrat:wght@400;500;600;700&family=Raleway:wght@400;500;600&display=swap" rel="stylesheet">
<style>
:root{
  --ink:#1c1c1e;
  --text:#3a3a3a;
  --white:#ffffff;
  --dark:#2f2e33;
  --footer:#2d2c30;
  --footer-base:#242327;
  --accent:#e0434a;
  --dot:#b9a7f0;
  --map-light:#e6e6e6;
  --map-mid:#d6d6d6;
  --pin:#e0343a;
}
*{margin:0;padding:0;box-sizing:border-box}
html,body{width:1200px;height:3371px;overflow:hidden;background:var(--white)}
body{position:relative;font-family:'Raleway',sans-serif;color:var(--text)}
.abs{position:absolute}
a{color:inherit;text-decoration:none}

/* header */
.site-header{position:absolute;left:0;top:0;width:1200px;height:104px;background:var(--white);border-bottom:4px solid var(--ink);z-index:2}
.brand-name{position:absolute;left:100px;top:33px;font-family:'Montserrat',sans-serif;font-size:28px;font-weight:500;line-height:34px;color:var(--ink);letter-spacing:.5px}
.main-nav a{position:absolute;top:38px;font-family:'Montserrat',sans-serif;font-size:13px;font-weight:500;color:var(--ink)}
.main-nav .is-active{border-bottom:2px solid var(--ink);padding-bottom:3px}
.login{position:absolute;left:1020px;top:31px;width:80px;height:34px;border:1.5px solid var(--ink);text-align:center;line-height:31px;font-family:'Montserrat',sans-serif;font-size:13px;font-weight:500;color:var(--ink)}

/* hero */
.hero{position:absolute;left:0;top:104px;width:1200px;height:577px}
.hero-title{position:absolute;left:0;top:240px;width:1200px;text-align:center;font-family:'Montserrat',sans-serif;font-size:27px;font-weight:500;color:var(--white);letter-spacing:.3px}
.hero-dots{position:absolute;left:553px;top:369px}
.hero-dots span{display:inline-block;width:11px;height:11px;border-radius:50%;background:var(--dot);margin-right:13px}

/* intro */
.intro p{position:absolute;top:748px;font-size:14px;line-height:28.5px;color:var(--text)}
.intro .col-left{left:125px;width:455px}
.intro .col-right{left:627px;width:460px}

/* commodities */
.commodities{position:absolute;left:0;top:1027px;width:1200px;height:652px;background:var(--dark);overflow:hidden}
.section-title-light{position:absolute;left:0;top:68px;width:1200px;text-align:center;font-family:'Montserrat',sans-serif;font-size:33px;font-weight:700;color:var(--white)}
.alloy-list{position:absolute;top:173px;list-style:none;font-family:'Montserrat',sans-serif;font-size:15px;font-weight:600;color:var(--white);line-height:27px}
.alloy-list li::before{content:"";display:inline-block;width:6px;height:6px;border-radius:50%;background:var(--white);margin-right:15px;vertical-align:middle;position:relative;top:-2px}
.step-label{position:absolute;width:140px;text-align:center;font-family:'Montserrat',sans-serif;font-size:13px;line-height:16px;text-transform:uppercase}
.commodities .step-label{color:var(--white)}

/* expertise */
.expertise-title{position:absolute;left:474px;top:1761px;font-family:'Montserrat',sans-serif;font-size:32px;font-weight:500;color:var(--ink);letter-spacing:.5px}
.expertise p{position:absolute;top:1847px;font-size:14px;line-height:24px;color:var(--text)}
.expertise .col-left{left:100px;width:420px}
.expertise .col-right{left:637px;width:465px}
.expertise .step-label{color:var(--ink)}

/* map */
.map-area{position:absolute;left:0;top:2243px;width:1200px;height:346px;background:linear-gradient(160deg,var(--map-light) 0%,var(--map-mid) 45%,var(--map-light) 70%,var(--map-mid) 100%)}
.map-toggle{position:absolute;left:0;top:0;height:22px;background:var(--white);font-family:'Raleway',sans-serif;font-size:10px;color:#333;box-shadow:0 1px 2px rgba(0,0,0,.25)}
.map-toggle span{display:inline-block;padding:0 9px;line-height:22px}
.map-toggle .is-on{font-weight:600}

/* contact card */
.contact-card{position:absolute;left:437px;top:2640px;width:325px;height:215px;border:1.5px solid #9a9a9a;text-align:center;font-family:'Montserrat',sans-serif;color:var(--text);font-style:normal}
.contact-card h3{margin-top:28px;font-size:17px;font-weight:500;color:var(--ink);letter-spacing:.5px}
.contact-card .rule{width:62px;height:2px;background:var(--accent);margin:14px auto 16px}
.contact-card p{font-size:12px;line-height:20px}
.contact-card .tel{margin-top:12px}
.contact-card .mail{margin-top:8px}

/* footer */
.site-footer{position:absolute;left:0;top:2915px;width:1200px;height:456px;background:var(--footer)}
.footer-heading{position:absolute;top:60px;font-family:'Montserrat',sans-serif;font-size:17px;font-weight:600;color:var(--white)}
.footer-links{position:absolute;top:100px;list-style:none;font-size:14px;line-height:28.5px;color:#c9c9c9}
.field{position:absolute;background:var(--white);font-size:12px;color:#777;padding:8px 10px}
.send{position:absolute;left:985px;top:290px;width:115px;height:36px;background:var(--ink);color:var(--white);font-family:'Montserrat',sans-serif;font-size:14px;font-weight:600;text-align:center;line-height:36px}
.footer-base{position:absolute;left:0;top:377px;width:1200px;height:79px;background:var(--footer-base);text-align:center;line-height:79px;font-size:12px;color:#d5d5d5}
</style>
</head>
<body>

<header class="site-header">
  <div class="brand-name">Velda Metals</div>
  <nav class="main-nav">
    <a class="is-active" href="#" style="left:509px">HOME</a>
    <a href="#" style="left:594px">ABOUT</a>
    <a href="#" style="left:684px">COMMODITIES</a>
    <a href="#" style="left:825px">SERVICES</a>
    <a href="#" style="left:929px">CONTACT</a>
  </nav>
  <a class="login" href="#">LOG IN</a>
</header>

<section class="hero">
  <svg class="abs" style="left:0;top:0" width="1200" height="577" role="img" aria-label="Photograph of a harbour with dock cranes silhouetted against a hazy dusk sky">
    <defs>
      <linearGradient id="heroSky" x1="0" y1="0" x2="0" y2="1">
        <stop offset="0" stop-color="#1f1a17"/>
        <stop offset=".45" stop-color="#5a4634"/>
        <stop offset=".7" stop-color="#8a6a48"/>
        <stop offset="1" stop-color="#2a221d"/>
      </linearGradient>
    </defs>
    <rect width="1200" height="577" fill="url(#heroSky)"/>
    <path d="M0 577 L0 545 Q600 480 1200 545 L1200 577 Z" fill="#ffffff"/>
  </svg>
  <h1 class="hero-title">Velda Metals supplies commodities to a global customer base</h1>
  <div class="hero-dots"><span></span><span></span><span></span><span></span></div>
</section>

<section class="intro">
  <p class="col-left">Velda Metals is a global commodities group with an experienced team and an established presence throughout the metal markets. With European processing facilities and trading offices, Velda has a strong focus on consolidating, processing, and trading a full range of physical metal commodities. Our network of clients and partners range from international metal producers, sovereigns, global manufacturers and industrial consumers.</p>
  <p class="col-right">Velda has an ethos of building long-term relationships throughout the global metal markets, based on transparency, trust and reliability. This culture underpins Velda's vertically integrated business, aligning it with its broad customer base throughout the commodity value chain.</p>
</section>

<section class="commodities">
  <svg class="abs" style="left:0;top:0" width="1200" height="652" role="img" aria-label="Photograph of a corrugated metal roof in dark grey light">
    <defs>
      <linearGradient id="roof" x1="0" y1="0" x2="1" y2="1">
        <stop offset="0" stop-color="#3a393e"/>
        <stop offset="1" stop-color="#6b6a70"/>
      </linearGradient>
    </defs>
    <polygon points="0,652 0,600 1200,190 1200,652" fill="url(#roof)" opacity=".85"/>
  </svg>
  <h2 class="section-title-light">FERRO-ALLOYS</h2>
  <ul class="alloy-list" style="left:272px">
    <li>Ferro-Chrome</li><li>Ferro-Manganese</li><li>Ferro-Molybdenum</li><li>Ferro-Silicon</li>
  </ul>
  <ul class="alloy-list" style="left:632px">
    <li>Ferro-Vanadium</li><li>Ferro- Titanium</li><li>Ferro-Cobalt</li>
  </ul>
  <svg class="abs" style="left:0;top:0" width="1200" height="652" aria-hidden="true">
    <polyline points="113,211 101,225 113,239" fill="none" stroke="#fff" stroke-width="2"/>
    <polyline points="1087,211 1099,225 1087,239" fill="none" stroke="#fff" stroke-width="2"/>
    <line x1="380" y1="390" x2="468" y2="390" stroke="#fff" stroke-width="1.5"/>
    <line x1="500" y1="390" x2="588" y2="390" stroke="#fff" stroke-width="1.5"/>
    <line x1="620" y1="390" x2="708" y2="390" stroke="#fff" stroke-width="1.5"/>
    <g font-family="Montserrat,sans-serif" font-size="15" text-anchor="middle">
      <circle cx="364" cy="390" r="16" fill="none" stroke="#fff" stroke-width="1.5"/><text x="364" y="395" fill="#fff">1</text>
      <circle cx="484" cy="390" r="16" fill="none" stroke="#fff" stroke-width="1.5"/><text x="484" y="395" fill="#fff">2</text>
      <circle cx="604" cy="390" r="16" fill="none" stroke="#fff" stroke-width="1.5"/><text x="604" y="395" fill="#fff">3</text>
      <circle cx="724" cy="390" r="16" fill="#fff"/><text x="724" y="395" fill="#2f2e33">4</text>
    </g>
  </svg>
  <div class="step-label" style="left:294px;top:422px">Copper</div>
  <div class="step-label" style="left:414px;top:422px">Aluminium</div>
  <div class="step-label" style="left:534px;top:422px">Semi-finished<br>alloys</div>
  <div class="step-label" style="left:654px;top:422px">Ferro-alloys</div>
</section>

<section class="expertise">
  <svg class="abs" style="left:416px;top:1760px" width="50" height="50" aria-hidden="true">
    <circle cx="25" cy="25" r="23" fill="none" stroke="#1c1c1e" stroke-width="1.5"/>
    <g fill="#1c1c1e">
      <circle cx="25" cy="17" r="3.5"/><circle cx="17" cy="25" r="3"/><circle cx="33" cy="25" r="3"/>
      <rect x="21" y="21.5" width="8" height="8" rx="2"/><rect x="13.5" y="29" width="7" height="7" rx="2"/><rect x="29.5" y="29" width="7" height="7" rx="2"/>
    </g>
  </svg>
  <h2 class="expertise-title">DIVERSE EXPERTISE</h2>
  <p class="col-left">Velda's team is experienced across the commodity value chain: commodity risk management, credit risk, commodity &amp; inventory finance solutions, marketing arrangements, commodity asset management and logistics management.</p>
  <p class="col-right">Velda's experienced team and vertically integrated business embraces commodities to its core, and aims to add value to all its partnerships, suppliers and customers by providing services that enhance their businesses profitability and optimises their commodity production.</p>
  <svg class="abs" style="left:0;top:2060px" width="1200" height="45" aria-hidden="true">
    <line x1="384" y1="22" x2="507" y2="22" stroke="#1c1c1e" stroke-width="1.2"/>
    <line x1="539" y1="22" x2="661" y2="22" stroke="#1c1c1e" stroke-width="1.2"/>
    <line x1="693" y1="22" x2="816" y2="22" stroke="#1c1c1e" stroke-width="1.2"/>
    <g font-family="Montserrat,sans-serif" font-size="15" text-anchor="middle">
      <circle cx="368" cy="22" r="16" fill="none" stroke="#1c1c1e" stroke-width="1.2"/><text x="368" y="27" fill="#1c1c1e">1</text>
      <circle cx="523" cy="22" r="16" fill="none" stroke="#1c1c1e" stroke-width="1.2"/><text x="523" y="27" fill="#1c1c1e">2</text>
      <circle cx="677" cy="22" r="16" fill="none" stroke="#1c1c1e" stroke-width="1.2"/><text x="677" y="27" fill="#1c1c1e">3</text>
      <circle cx="832" cy="22" r="16" fill="#1c1c1e"/><text x="832" y="27" fill="#fff">4</text>
    </g>
  </svg>
  <div class="step-label" style="left:298px;top:2114px">Trading<br>&amp; sourcing</div>
  <div class="step-label" style="left:453px;top:2114px">Processing<br>&amp; consolidating</div>
  <div class="step-label" style="left:607px;top:2114px">Outsourced<br>solutions</div>
  <div class="step-label" style="left:762px;top:2114px">Diverse<br>expertise</div>
</section>

<section class="map-area" role="img" aria-label="Interactive street map of the city area around the office, with a pin marking the Velda Metals location">
  <div class="map-toggle"><span class="is-on">Map</span><span>Satellite</span></div>
  <svg class="abs" style="left:620px;top:129px" width="24" height="34" aria-hidden="true">
    <path d="M12 33 C12 33 1 18 1 11 A11 11 0 0 1 23 11 C23 18 12 33 12 33 Z" fill="var(--pin)"/>
    <circle cx="12" cy="11" r="4" fill="#8a1518"/>
  </svg>
</section>

<address class="contact-card">
  <h3>VELDA METALS</h3>
  <div class="rule"></div>
  <p>Unit 7, Larkfield Trade Park<br>Hollowmere, HX4 2QT, United Kingdom</p>
  <p class="tel">Tel :+44(0)7700 900412</p>
  <p class="mail">contact@veldametals.com</p>
</address>

<footer class="site-footer">
  <h4 class="footer-heading" style="left:100px">Sitemap</h4>
  <ul class="footer-links" style="left:100px">
    <li>Home</li><li>About</li><li>Commodities</li><li>Services</li><li>Contact</li><li>Login</li>
  </ul>
  <h4 class="footer-heading" style="left:313px">Social</h4>
  <ul class="footer-links" style="left:313px">
    <li>Linkora</li><li>Chirpline</li>
  </ul>
  <h4 class="footer-heading" style="left:565px">Get In Touch</h4>
  <div class="field" style="left:567px;top:100px;width:260px;height:33px">Name</div>
  <div class="field" style="left:841px;top:100px;width:259px;height:33px">Email</div>
  <div class="field" style="left:567px;top:148px;width:533px;height:33px">Phone</div>
  <div class="field" style="left:567px;top:190px;width:533px;height:83px">Message</div>
  <div class="send">SEND</div>
  <div class="footer-base">© Copyright-2018 Velda Metals.All rights reserved.</div>
</footer>

</body>
</html>
```